Body therapist needs a business card

I need a card for my business which is teaching trainings in body therapy, the company is called Wexcombe Educational Group. I teach to massage therapists around Australia, South East Asia and the USA. I am attaching my logo which will guide you as to what colours I would like to have you consider. Please consult my website to find out more about what I do. www.corvantela.com.au

My name is Daniel Wexcombe. My phone number is (03) 9417 2608 or 0461753208. email is info@corvantela.com.au

```html
<!DOCTYPE html>
<html lang="en">
<head>
<meta charset="utf-8">
<title>Wexcombe Educational Group – Business Card</title>
<link rel="stylesheet" href="https://fonts.googleapis.com/css2?family=Cabin:wght@600&family=Questrial&display=swap">
<style>
  :root {
    --backdrop: #e0d8d7;
    --copper: #b0671f;
    --copper-deep: #a35d1d;
    --cream: #efe6dc;
    --tan: #c38a4f;
    --brown: #7c4a1b;
    --card-white: #f7f7f7;
    --card-grey: #e9e9eb;
    --faint: #e4d9cd;
  }
  * { margin: 0; padding: 0; box-sizing: border-box; }
  html, body {
    width: 1200px; height: 1200px; overflow: hidden;
    background: var(--backdrop);
  }
  .canvas { position: relative; width: 1200px; height: 1200px; }

  .card {
    position: absolute; left: 250px; width: 700px; height: 400px; overflow: hidden;
  }
  .card--front {
    top: 147px;
    background: linear-gradient(100deg, var(--copper) 0%, var(--copper-deep) 100%);
  }
  .card--back {
    top: 652px;
    background: linear-gradient(160deg, #ffffff 0%, var(--card-white) 55%, var(--card-grey) 100%);
  }

  /* front decoration */
  .front-emblem {
    position: absolute; left: 348px; top: 83px;
    width: 272px; height: 272px; border-radius: 50%;
    background: linear-gradient(135deg, var(--tan) 10%, #d2b08c 60%, var(--cream) 100%);
    display: flex; align-items: center; justify-content: center;
  }
  .front-emblem__name {
    font-family: "Questrial", sans-serif;
    font-size: 34px; letter-spacing: 1px;
    color: var(--copper-deep);
  }

  /* back: brand block */
  .brand-dot {
    position: absolute; left: 66px; top: 40px;
    width: 96px; height: 96px; border-radius: 50%;
    background: var(--brown);
  }
  .brand-name {
    position: absolute; left: 35px; top: 160px;
    font-family: "Questrial", sans-serif; color: var(--brown);
    line-height: 1;
  }
  .brand-name__main { display: block; font-size: 27px; letter-spacing: -0.5px; }
  .brand-name__sub { display: block; font-size: 16px; margin-top: 6px; letter-spacing: -0.3px; }

  .person {
    position: absolute; left: 35px; top: 243px;
    font-family: "Cabin", sans-serif; font-weight: 600;
    font-size: 23px; color: var(--brown);
  }
  .contact {
    position: absolute; left: 35px; top: 284px;
    font-family: "Cabin", sans-serif; font-weight: 600;
    font-size: 17px; color: var(--brown); list-style: none;
  }
  .contact__row { display: flex; align-items: flex-start; gap: 9px; margin-bottom: 9px; }
  .contact__icon { width: 26px; height: 20px; flex: none; margin-top: 1px; }
  .contact__lines span { display: block; line-height: 24px; }

  /* back: faint decoration */
  .back-emblem {
    position: absolute; left: 396px; top: 55px;
    width: 258px; height: 258px; border-radius: 50%;
    background: var(--faint);
    display: flex; align-items: center; justify-content: center;
  }
  .back-emblem__name {
    font-family: "Questrial", sans-serif; font-size: 30px;
    color: #f4efe9;
  }

  .social {
    position: absolute; right: 42px; top: 332px;
    display: flex; gap: 10px;
    font-family: "Cabin", sans-serif; font-weight: 600;
    font-size: 12px; color: var(--brown);
  }
</style>
</head>
<body>
<main class="canvas">

  <section class="card card--front" aria-label="Card front">
    <div class="front-emblem">
      <span class="front-emblem__name">Wexcombe</span>
    </div>
  </section>

  <section class="card card--back" aria-label="Card back">
    <div class="brand-dot"></div>
    <h1 class="brand-name">
      <span class="brand-name__main">WEXCOMBE</span>
      <span class="brand-name__sub">EDUCATIONAL GROUP</span>
    </h1>

    <p class="person">Daniel Wexcombe</p>

    <ul class="contact">
      <li class="contact__row">
        <svg class="contact__icon" viewBox="0 0 26 18" aria-hidden="true">
          <rect x="0" y="0" width="26" height="18" fill="#7c4a1b"/>
          <polyline points="1,1 13,10 25,1" fill="none" stroke="#f7f7f7" stroke-width="2"/>
          <line x1="1" y1="17" x2="10" y2="8" stroke="#f7f7f7" stroke-width="1.6"/>
          <line x1="25" y1="17" x2="16" y2="8" stroke="#f7f7f7" stroke-width="1.6"/>
        </svg>
        <span class="contact__lines"><span>info@corvantela.com.au</span></span>
      </li>
      <li class="contact__row">
        <svg class="contact__icon" viewBox="0 0 26 24" aria-hidden="true">
          <path d="M4 3 L8 2 L10 8 L7 10 C8.5 13.5 10.5 15.5 14 17 L16 14 L22 16 L21 20 C12 22 2 12 4 3 Z" fill="#7c4a1b"/>
          <path d="M14 2 A8 8 0 0 1 22 10" fill="none" stroke="#7c4a1b" stroke-width="2"/>
          <path d="M14 6 A4 4 0 0 1 18 10" fill="none" stroke="#7c4a1b" stroke-width="2"/>
        </svg>
        <span class="contact__lines">
          <span>(03) 9417 2608</span>
          <span>0461753208</span>
        </span>
      </li>
    </ul>

    <div class="back-emblem">
      <span class="back-emblem__name">Wexcombe</span>
    </div>

    <div class="social">
      <span class="social__name">Clipora</span>
      <span class="social__name">Kinlink</span>
    </div>
  </section>

</main>
</body>
</html>
```